Corvell Bookkeeping Services business cards

looking for a double sided business card design. My logo is attached. I am looking for a design similar to the attached. Keen to see what my logo in white on the blue background would look like.

```html
<!DOCTYPE html>
<html lang="en">
<head>
<meta charset="utf-8">
<title>Corvell Bookkeeping Services – Business Cards</title>
<link href="https://fonts.googleapis.com/css2?family=Montserrat:wght@400;500;800&display=swap" rel="stylesheet">
<style>
  :root {
    --bg: #a9a5a6;
    --green: #9cc43a;
    --navy: #1d3a7a;
    --navy-light: #2a4f9a;
    --navy-deep: #15295a;
    --ink: #1e1e24;
    --white: #ffffff;
    --faint: #f3f6ea;
  }
  * { box-sizing: border-box; margin: 0; padding: 0; }
  html, body { width: 1200px; height: 900px; overflow: hidden; }
  body {
    background: var(--bg);
    font-family: "Montserrat", Arial, sans-serif;
    position: relative;
  }
  .card {
    position: absolute;
    left: 260px;
    width: 680px;
    height: 388px;
    border-radius: 22px;
    overflow: hidden;
    box-shadow: 0 10px 26px rgba(0,0,0,0.22);
  }
  .card-front { top: 48px; background: var(--navy); }
  .card-back  { top: 468px; background: var(--white); }

  .pattern-fill {
    position: absolute; inset: 0;
    background: linear-gradient(135deg, var(--navy-light) 0%, var(--navy) 50%, var(--navy-deep) 100%);
  }
  .front-brand {
    position: absolute; left: 50%; top: 50%;
    transform: translate(-50%, -50%);
    display: flex; align-items: center; gap: 14px;
    white-space: nowrap;
  }
  .brand-square {
    flex: none;
    width: 30px; height: 30px; border-radius: 4px;
  }
  .front-brand .brand-square { background: var(--white); }
  .front-brand .brand-name {
    color: var(--white); font-weight: 800; font-size: 24px;
  }

  .back-watermark {
    position: absolute; right: 40px; top: 30px;
    width: 330px; height: 250px; border-radius: 40px;
    background: radial-gradient(ellipse at center, var(--faint) 0%, rgba(255,255,255,0) 75%);
  }
  .back-brand {
    position: absolute; left: 46px; top: 54px;
    display: flex; align-items: center; gap: 14px;
    white-space: nowrap;
  }
  .back-brand .brand-square { background: var(--navy); }
  .back-brand .brand-name { color: var(--navy); font-weight: 800; font-size: 24px; }

  .person { position: absolute; left: 46px; top: 160px; }
  .person-name { color: var(--navy); font-weight: 800; font-size: 26px; }
  .person-role { color: var(--ink); font-size: 15px; margin-top: 2px; }

  .contact-list { position: absolute; left: 46px; top: 238px; list-style: none; }
  .contact-list li {
    display: flex; align-items: center; gap: 12px;
    font-size: 16px; color: var(--ink); line-height: 30px;
  }
  .contact-list svg { width: 16px; height: 16px; fill: var(--green); }

  .address {
    position: absolute; right: 40px; top: 196px;
    text-align: right; font-size: 15px; line-height: 22px; color: var(--ink);
  }
</style>
</head>
<body>
  <section class="card card-front">
    <div class="pattern-fill" role="img" aria-label="Repeating tone-on-tone brand emblem pattern in blues"></div>
    <div class="front-brand">
      <span class="brand-square"></span>
      <span class="brand-name">Corvell Bookkeeping Services</span>
    </div>
  </section>

  <section class="card card-back">
    <div class="back-watermark" role="img" aria-label="Faint oversized brand emblem decoration"></div>
    <div class="back-brand">
      <span class="brand-square"></span>
      <span class="brand-name">Corvell Bookkeeping Services</span>
    </div>
    <div class="person">
      <p class="person-name">Tarek Holloway</p>
      <p class="person-role">Owner</p>
    </div>
    <ul class="contact-list">
      <li><svg viewBox="0 0 16 16"><path d="M3 1l3 3-2 2c1 2 3 4 5 5l2-2 3 3-2 3C6 15 1 10 1 3z"/></svg>(718) 555-0142</li>
      <li><svg viewBox="0 0 16 16"><path d="M4 0h8a1 1 0 0 1 1 1v14a1 1 0 0 1-1 1H4a1 1 0 0 1-1-1V1a1 1 0 0 1 1-1zm1 2v10h6V2z"/></svg>(917) 555-0178</li>
      <li><svg viewBox="0 0 16 16"><path d="M0 3h16v10H0zm1 1l7 5 7-5z"/></svg>info@corvell.com</li>
      <li><svg viewBox="0 0 16 16"><circle cx="8" cy="8" r="7"/></svg>www.corvell.com</li>
    </ul>
    <p class="address">1480 Ridgeline Avenue, Ste<br>210 Knoxville, TN 37919</p>
  </section>
</body>
</html>
```